" - Oferecemos os mais diversos ramos de seguros como: auto | frota | residencial | vida | empresarial | saúde | previdência | RC | viagem e outros. - sólida parceria com as principais Seguradoras de todo Brasil como QRV, Vendral, Tavorino Seguros, Plenx, KWT, Ornavia, Garelo, Pirula, Dekal, Vitalcoro, Felpa Norvita Quelda, Nortiz e outras. Por isto é possível encontrar os melhores produtos do mercado e o melhor custo-benefício na hora de analisar uma proposta. "

```html
<!DOCTYPE html>
<html lang="pt-BR">
<head>
<meta charset="utf-8">
<title>Mix Completo de Seguros</title>
<link rel="stylesheet" href="https://fonts.googleapis.com/css2?family=Montserrat:wght@300;700;800;900&display=swap">
<style>
  :root {
    --bg-deep: #0a2f3b;
    --bg-mid: #12535f;
    --bg-light: #1f7f86;
    --panel-top: #0f4756;
    --panel-bottom: #0b3642;
    --panel-glow: #1b6e78;
    --white: #ffffff;
    --frame: rgba(255, 255, 255, 0.85);
    --badge-text: #0f4756;
    --reaction-blue: #3b7ddd;
    --reaction-yellow: #f4c542;
    --reaction-pink: #f0557e;
    --reaction-orange: #f29a3a;
  }
  * { margin: 0; padding: 0; box-sizing: border-box; }
  html, body { width: 1200px; height: 1200px; overflow: hidden; }
  body {
    position: relative;
    font-family: "Montserrat", sans-serif;
    background: radial-gradient(circle at 50% 40%, var(--bg-light) 0%, var(--bg-mid) 45%, var(--bg-deep) 100%);
    color: var(--white);
  }
  .pack-label {
    position: absolute;
    top: 38px; left: 0; width: 100%;
    text-align: center;
    font-weight: 800;
    font-size: 30px;
    letter-spacing: 4px;
  }
  .post {
    position: absolute;
    left: 84px; top: 92px;
    width: 1032px; height: 1032px;
    background: linear-gradient(180deg, var(--panel-top) 0%, var(--panel-bottom) 70%, var(--panel-glow) 100%);
    box-shadow: 0 20px 50px rgba(0, 0, 0, 0.35);
    overflow: hidden;
  }
  .post-photo {
    position: absolute; inset: 0;
    background:
      radial-gradient(ellipse at 25% 20%, rgba(120, 190, 200, 0.35) 0%, transparent 45%),
      radial-gradient(ellipse at 30% 75%, rgba(150, 210, 215, 0.25) 0%, transparent 50%),
      radial-gradient(ellipse at 75% 85%, rgba(60, 140, 155, 0.3) 0%, transparent 50%);
  }
  .post-frame {
    position: absolute;
    left: 41px; top: 58px;
    width: 967px; height: 858px;
    border: 3px solid var(--frame);
    border-radius: 40px;
  }
  .headline-icon {
    position: absolute;
    left: 464px; top: 313px;
    width: 130px; height: 125px;
  }
  .headline-small {
    position: absolute;
    left: 252px; top: 498px;
    font-weight: 300;
    font-size: 47px;
    letter-spacing: 1px;
    line-height: 1;
    white-space: nowrap;
  }
  .headline-big {
    position: absolute;
    left: 307px; top: 552px;
    font-weight: 900;
    font-size: 88px;
    line-height: 1;
    letter-spacing: 1px;
    white-space: nowrap;
  }
  .brand-badge {
    position: absolute;
    left: 840px; top: 996px;
    width: 216px; height: 144px;
    background: var(--white);
    display: flex; align-items: center; justify-content: center;
  }
  .brand-name {
    color: var(--badge-text);
    font-weight: 700;
    font-size: 38px;
    letter-spacing: 1px;
  }
  .reaction { position: absolute; border-radius: 50%; }
  .reaction-a { left: 36px; top: 180px; width: 50px; height: 50px; background: var(--reaction-blue); }
  .reaction-b { left: 1052px; top: 260px; width: 110px; height: 110px; background: var(--reaction-yellow); opacity: 0.9; }
  .reaction-c { left: 1032px; top: 852px; width: 120px; height: 120px; background: var(--reaction-pink); }
  .reaction-d { left: -2px; top: 934px; width: 100px; height: 100px; background: var(--reaction-orange); opacity: 0.9; }
  .reaction-e { left: 86px; top: 1088px; width: 44px; height: 44px; background: var(--reaction-blue); }
</style>
</head>
<body>
  <div class="pack-label">PACK POST - SOCIAL MEDIA</div>

  <section class="post">
    <div class="post-photo" role="img" aria-label="Foto em tons de azul-petróleo: mãos protegendo a silhueta de uma família"></div>
    <div class="post-frame"></div>

    <svg class="headline-icon" viewBox="0 0 130 120" fill="none" stroke="#ffffff" stroke-width="6" stroke-linecap="round" stroke-linejoin="round">
      <path d="M65 70 C40 52 28 42 28 28 C28 16 37 8 47 8 C55 8 61 13 65 19 C69 13 75 8 83 8 C93 8 102 16 102 28 C102 42 90 52 65 70 Z" fill="#ffffff"/>
      <polyline points="30,34 50,34 56,24 64,46 72,28 78,34 100,34" stroke="#0f4756" stroke-width="5"/>
      <path d="M8 92 L28 92 C40 92 48 96 56 100 L76 100 C82 100 82 108 76 108 L54 108"/>
      <path d="M28 112 L70 116 C88 114 104 100 122 86"/>
    </svg>
    <div class="headline-small">MIX COMPLETO DE</div>
    <div class="headline-big">SEGUROS</div>
  </section>

  <div class="reaction reaction-a" role="img" aria-label="Ícone de reação azul"></div>
  <div class="reaction reaction-b" role="img" aria-label="Ícone de reação amarelo"></div>
  <div class="reaction reaction-c" role="img" aria-label="Ícone de reação rosa"></div>
  <div class="reaction reaction-d" role="img" aria-label="Ícone de reação laranja"></div>
  <div class="reaction reaction-e" role="img" aria-label="Ícone de reação azul"></div>

  <div class="brand-badge">
    <span class="brand-name">NORVEL</span>
  </div>
</body>
</html>
```